Ground breaking athletic gear company needs a kick ass business card

We are an American start up athletic gear company that uses a medically proven biohack to boost athletic performance. Heat kills strength and endurance. Our gear helps athletes manage heat better and ultimatley can improve them by up to 10% instantly. Nothing like it out there! Launching this summer.
We are looking for a modern, minimalist design that captures a sporty edge. Check out www.velmarunwear.com, @velmarunwear on instagram for more ideas.

Target Market(s)

25-35 year olds, male and female athletes, vaultlift athletes, competitive runners

Industry/Entity Type

Business

Contact Information for Business Card

Dorian Pellham
Founder
dorianp@velmarunwear.com
www.VelmaRunwear.com
+1 (555) 014-2286

Font styles to use
Sans Serif

Requirements
Must have
• Logo and icon
• All contact information
• dorianp@velmarunwear.com
• +1 (555) 019-4471 M
• +1 (555) 014-2286
Nice to have
• Tag line : "Cool & Conquer"

```html
<!DOCTYPE html>
<html lang="en">
<head>
<meta charset="utf-8">
<title>Velma Runwear — Business Card</title>
<link href="https://fonts.googleapis.com/css2?family=Source+Sans+3:wght@400;600&display=swap" rel="stylesheet">
<style>
  :root {
    --page: #ffffff;
    --card: #000000;
    --ink: #ffffff;
    --card-radius: 72px;
  }
  * { margin: 0; padding: 0; box-sizing: border-box; }
  html, body {
    width: 1200px;
    height: 900px;
    overflow: hidden;
    background: var(--page);
    font-family: "Source Sans 3", "Myriad Pro", Arial, sans-serif;
    color: var(--ink);
  }
  .canvas { position: relative; width: 1200px; height: 900px; }

  .card {
    position: absolute;
    top: 200px;
    width: 310px;
    height: 502px;
    background: var(--card);
  }
  .card--front {
    left: 265px;
    border-radius: var(--card-radius) 0 var(--card-radius) 0;
  }
  .card--back {
    left: 641px;
    width: 309px;
    border-radius: 0 var(--card-radius) 0 var(--card-radius);
  }

  .brand {
    position: absolute;
    left: 0;
    right: 0;
    display: flex;
    align-items: center;
    justify-content: center;
    gap: 10px;
    font-weight: 400;
    text-transform: uppercase;
    letter-spacing: 0.14em;
    color: var(--ink);
  }
  .brand__mark {
    width: 14px;
    height: 14px;
    border: 1.5px solid var(--ink);
  }
  .card--front .brand { top: 108px; font-size: 14px; }
  .card--back .brand { top: 128px; font-size: 16px; }

  .contact {
    position: absolute;
    left: 37px;
    top: 336px;
  }
  .contact__name {
    font-size: 18.5px;
    font-weight: 600;
    line-height: 1.2;
  }
  .contact__role {
    font-size: 13.5px;
    font-weight: 400;
    margin-top: 2px;
  }
  .contact__list {
    list-style: none;
    margin-top: 17px;
  }
  .contact__item {
    display: flex;
    align-items: center;
    gap: 7px;
    font-size: 13.5px;
    height: 20.5px;
    white-space: nowrap;
  }
  .contact__icon { width: 11px; height: 11px; fill: var(--ink); flex: none; }

  .social {
    position: absolute;
    left: 0;
    right: 0;
    top: 410px;
    display: flex;
    align-items: center;
    justify-content: center;
    gap: 10px;
    font-size: 15px;
    font-weight: 400;
  }
  .social__dot {
    width: 36px;
    height: 36px;
    border-radius: 50%;
    background: var(--ink);
  }
</style>
</head>
<body>
<main class="canvas">

  <section class="card card--front" aria-label="Business card front">
    <div class="brand"><span class="brand__mark"></span>Velma Runwear</div>

    <div class="contact">
      <p class="contact__name">Dorian Pellham</p>
      <p class="contact__role">Founder</p>
      <ul class="contact__list">
        <li class="contact__item">
          <svg class="contact__icon" viewBox="0 0 24 24" aria-hidden="true"><path d="M6.6 10.8a15.1 15.1 0 0 0 6.6 6.6l2.2-2.2c.3-.3.7-.4 1-.2 1.1.4 2.3.6 3.6.6.6 0 1 .4 1 1V20c0 .6-.4 1-1 1A17 17 0 0 1 3 4c0-.6.4-1 1-1h3.5c.6 0 1 .4 1 1 0 1.3.2 2.5.6 3.6.1.3 0 .7-.2 1z"/></svg>
          +1 (555) 014-2286
        </li>
        <li class="contact__item">
          <svg class="contact__icon" viewBox="0 0 24 24" aria-hidden="true"><rect x="6" y="1" width="12" height="22" rx="2"/><rect x="8" y="4" width="8" height="13" fill="#000"/><circle cx="12" cy="20" r="1.2" fill="#000"/></svg>
          +1 (555) 019-4471 M
        </li>
        <li class="contact__item">
          <svg class="contact__icon" viewBox="0 0 24 24" aria-hidden="true"><path d="M2 5h20v14H2z"/><path d="M3 7l9 6.5L21 7" stroke="#000" stroke-width="2" fill="none"/></svg>
          dorianp@velmarunwear.com
        </li>
        <li class="contact__item">
          <svg class="contact__icon" viewBox="0 0 24 24" aria-hidden="true"><circle cx="12" cy="12" r="10"/><path d="M2 12h20M12 2c3 3 3 17 0 20M12 2c-3 3-3 17 0 20" stroke="#000" stroke-width="1.6" fill="none"/></svg>
          www.VelmaRunwear.com
        </li>
      </ul>
    </div>
  </section>

  <section class="card card--back" aria-label="Business card back">
    <div class="brand"><span class="brand__mark"></span>Velma Runwear</div>
    <div class="social"><span class="social__dot"></span>@velmarunwear</div>
  </section>

</main>
</body>
</html>
```